We Buy Houses Postcard Design

Harborline Estate Traders is one of Baltimore‘s top real estate investing groups because we treat buyers and sellers like real people; not like numbers on a spreadsheet. We specialize in buying distressed properties including multi-family, commercial, retail, single family, and bank REO’s from sellers who need to sell fast. Our website is www.harborlineestatetraders.com. Our phone number is (443) 517-2094. Both need to be on the card. Front and back sides are to be printed. Front full color, back black and white. We want our logo on the design somewhere. The logo can be found on the website. If you need the original files ask me for them. See attached as examples. Return address should be 487 W Quillfern Ave, Suite 316, Baltimore, MD 21202. My name is Marcus. Address label is 1" x 2-5/8". Please leave room for it and postage on the back side.

Industry/Entity Type

Real Estate

```html
<!DOCTYPE html>
<html lang="en">
<head>
<meta charset="utf-8">
<title>Harborline Estate Traders – Postcard Back</title>
<link href="https://fonts.googleapis.com/css2?family=Arimo:wght@400;700&display=swap" rel="stylesheet">
<style>
  :root {
    --paper: #ffffff;
    --frame: #8a8a8a;
    --ink: #222222;
    --headline: #4a4a4a;
    --icon-fill: #3e4544;
    --icon-edge: #2a302f;
  }
  * { margin: 0; padding: 0; box-sizing: border-box; }
  html, body {
    width: 1200px;
    height: 862px;
    overflow: hidden;
    background: var(--paper);
  }
  .postcard {
    position: relative;
    width: 1200px;
    height: 862px;
    background: var(--paper);
    border: 1px solid var(--frame);
    font-family: "Arimo", Arial, sans-serif;
    color: var(--ink);
  }
  .site-url {
    position: absolute;
    left: 73px;
    top: 66px;
    font-size: 25px;
    line-height: 30px;
    font-weight: 400;
  }
  .headline {
    position: absolute;
    left: 73px;
    top: 140px;
    font-size: 53px;
    line-height: 58px;
    font-weight: 700;
    color: var(--headline);
    letter-spacing: -0.3px;
  }
  .headline .headline-emphasis {
    display: block;
    font-size: 75px;
    line-height: 80px;
    margin-left: -3px;
  }
  .return-address {
    position: absolute;
    left: 73px;
    top: 462px;
    font-size: 26px;
    line-height: 31px;
    font-style: normal;
  }
  .return-address .contact-name {
    font-weight: 700;
    display: block;
  }
  .social {
    position: absolute;
    left: 73px;
    top: 600px;
  }
  .social-title {
    font-size: 18px;
    line-height: 22px;
    font-weight: 700;
    letter-spacing: -0.4px;
    margin-bottom: 9px;
  }
  .social-list {
    display: flex;
    gap: 3px;
    list-style: none;
  }
  .social-tile {
    width: 41px;
    height: 41px;
    background: var(--icon-fill);
    border: 1px solid var(--icon-edge);
    border-radius: 3px;
  }
</style>
</head>
<body>
  <main class="postcard">
    <p class="site-url">www.harborlineestatetraders.com</p>

    <h1 class="headline">
      We are<br>
      interested in<br>
      buying your
      <span class="headline-emphasis">House!</span>
    </h1>

    <address class="return-address">
      <span class="contact-name">Mr. Marcus</span>
      487 W Quillfern Ave.<br>
      Suite 316, Baltimore<br>
      MD 21202.
    </address>

    <section class="social">
      <p class="social-title">Connect With Us!</p>
      <ul class="social-list">
        <li class="social-tile" aria-label="Social profile"></li>
        <li class="social-tile" aria-label="Social profile"></li>
        <li class="social-tile" aria-label="Social profile"></li>
        <li class="social-tile" aria-label="Social profile"></li>
        <li class="social-tile" aria-label="Social profile"></li>
      </ul>
    </section>
  </main>
</body>
</html>
```